Essential Oil 15ml - package of 6

Design of a box of 6 different essential oils.
+ design of the bottle stickers
My bottles are 15ml clear blue glass.

The pictures attached are my competitors...

Target Market(s)

BRAMBLEWICK USA

Font styles to use
Serif

Requirements
Must have
• Our logo + "essential oil" and type (lavender, eucalyptus etc....)
• 15ml - 0.50 fl.oz.
• special color for the oil type.

```html
<!DOCTYPE html>
<html lang="en">
<head>
<meta charset="utf-8">
<title>Mor Hadar Essential Oil Labels</title>
<link rel="stylesheet" href="https://fonts.googleapis.com/css2?family=Alegreya+Sans:wght@700&family=Delius&display=swap">
<style>
  :root {
    --page: #ffffff;
    --label-dark: #25252f;
    --label-blue: #2c2b5a;
    --ink-dim: #3b379f;
    --lavender: #c0267e;
    --lemon: #f2e400;
    --lime: #c6d634;
    --rose: #e6284a;
    --eucalyptus: #3b8a78;
    --apple: #e8e67c;
  }
  html, body {
    margin: 0;
    padding: 0;
    width: 1200px;
    height: 2528px;
    overflow: hidden;
    background: var(--page);
  }
  .sheet {
    position: relative;
    width: 1200px;
    height: 2528px;
  }
  .label {
    position: absolute;
    width: 305px;
    height: 436px;
    background: linear-gradient(90deg, var(--label-dark) 0%, var(--label-dark) 45%, var(--label-blue) 100%);
    font-family: "Delius", cursive;
    color: var(--ink-dim);
    text-align: center;
  }
  .label > * {
    position: absolute;
    left: 0;
    right: 0;
    margin: 0;
    white-space: nowrap;
  }
  .brand-mark {
    top: 22px;
    left: 119px;
    right: auto;
    width: 66px;
    height: 66px;
    border-radius: 50%;
    background: var(--ink-dim);
  }
  .brand-name {
    top: 110px;
    font-family: "Alegreya Sans", sans-serif;
    font-weight: 700;
    font-size: 40px;
    line-height: 48px;
  }
  .oil-kind {
    top: 180px;
    font-size: 22px;
    line-height: 28px;
    letter-spacing: 0.5px;
  }
  .oil-name {
    top: 238px;
    font-size: 34px;
    line-height: 40px;
  }
  .grade {
    top: 310px;
    font-size: 22px;
    line-height: 32px;
  }
  .volume {
    top: 404px;
    font-size: 17px;
    line-height: 22px;
  }
  .col-1 { left: 111px; }
  .col-2 { left: 448px; }
  .col-3 { left: 781px; }
  .row-1 { top: 720px; }
  .row-2 { top: 1826px; }
  .lavender .oil-name { color: var(--lavender); }
  .lemon .oil-name { color: var(--lemon); }
  .lime .oil-name { color: var(--lime); }
  .rose .oil-name { color: var(--rose); }
  .eucalyptus .oil-name { color: var(--eucalyptus); }
  .apple .oil-name { color: var(--apple); }
</style>
</head>
<body>
<main class="sheet">
  <section class="label lavender row-1 col-1">
    <div class="brand-mark"></div>
    <p class="brand-name">Mor Hadar</p>
    <p class="oil-kind">100% ESSENTIAL OIL</p>
    <p class="oil-name">LAVANDER</p>
    <p class="grade">PURE THERAPEUTIC<br>GRADE</p>
    <p class="volume">15 ml</p>
  </section>
  <section class="label lemon row-1 col-2">
    <div class="brand-mark"></div>
    <p class="brand-name">Mor Hadar</p>
    <p class="oil-kind">100% ESSENTIAL OIL</p>
    <p class="oil-name">LEMON</p>
    <p class="grade">PURE THERAPEUTIC<br>GRADE</p>
    <p class="volume">15 ml</p>
  </section>
  <section class="label lime row-1 col-3">
    <div class="brand-mark"></div>
    <p class="brand-name">Mor Hadar</p>
    <p class="oil-kind">100% ESSENTIAL OIL</p>
    <p class="oil-name">LIME</p>
    <p class="grade">PURE THERAPEUTIC<br>GRADE</p>
    <p class="volume">15 ml</p>
  </section>
  <section class="label rose row-2 col-1">
    <div class="brand-mark"></div>
    <p class="brand-name">Mor Hadar</p>
    <p class="oil-kind">100% ESSENTIAL OIL</p>
    <p class="oil-name">ROSE</p>
    <p class="grade">PURE THERAPEUTIC<br>GRADE</p>
    <p class="volume">15 ml</p>
  </section>
  <section class="label eucalyptus row-2 col-2">
    <div class="brand-mark"></div>
    <p class="brand-name">Mor Hadar</p>
    <p class="oil-kind">100% ESSENTIAL OIL</p>
    <p class="oil-name">EUCALYPTUS</p>
    <p class="grade">PURE THERAPEUTIC<br>GRADE</p>
    <p class="volume">15 ml</p>
  </section>
  <section class="label apple row-2 col-3">
    <div class="brand-mark"></div>
    <p class="brand-name">Mor Hadar</p>
    <p class="oil-kind">100% ESSENTIAL OIL</p>
    <p class="oil-name">APPLE</p>
    <p class="grade">PURE THERAPEUTIC<br>GRADE</p>
    <p class="volume">15 ml</p>
  </section>
</main>
</body>
</html>
```